A postcard needed for a kids gym

We are a kids gym opening soon. We are called Brightleap Kids Gym. Here is the website so that you can get more details on what it is we will be doing. www.Brightleapkidsgym.example I am including a screen shot of wallpaper we are using on two walls that will be prominently displayed in our building. I was wondering if the wall paper can somehow be included in the postcard as a soft background or something?no postage or mail info needed as this will be passed out by hand. I am also sending our logo and colors. Thank you for your help, and we look forward to hearing and seeing what you have to present. Sincerely,Rosalind

Target Market(s)

Parents

Industry/Entity Type

Childcare

Requirements
Must have
• "Opening soon"

```html
<!DOCTYPE html>
<html lang="en">
<head>
<meta charset="utf-8">
<title>Brightleap Kids Gym – Opening Soon Postcard</title>
<link rel="stylesheet" href="https://fonts.googleapis.com/css2?family=Fredoka:wght@400;500&family=Josefin+Sans:wght@300&display=swap">
<style>
  :root {
    --backdrop: #6b6e72;
    --card-white: #ffffff;
    --brand-blue: #2ea3e6;
    --brand-blue-deep: #1f7fcf;
    --brand-orange: #f2a93b;
    --ink-soft-blue: #4ab0e8;
    --photo-red: #e2412c;
    --photo-green: #2fa24a;
    --photo-blue: #2a63d6;
    --photo-purple: #8a3ab5;
    --forest-light: #f3f4f4;
    --forest-mid: #dcdfdf;
  }
  * { margin: 0; padding: 0; box-sizing: border-box; }
  html, body { width: 900px; height: 1200px; overflow: hidden; }
  body {
    background: var(--backdrop);
    position: relative;
    font-family: "Fredoka", "Arial Rounded MT Bold", sans-serif;
  }
  .postcard {
    position: absolute;
    width: 625px;
    height: 500px;
    background: var(--card-white);
    overflow: hidden;
  }
  .postcard--front { left: 95px; top: 50px; }
  .postcard--back  { left: 185px; top: 628px; }

  .front-art { position: absolute; inset: 0; }
  .photo-area { position: absolute; left: 0; top: 0; width: 625px; height: 360px; }

  .opening-tab {
    position: absolute;
    left: 82px;
    top: 268px;
    width: 262px;
    height: 66px;
    background: linear-gradient(180deg, var(--brand-blue) 0%, var(--brand-blue-deep) 100%);
    border-radius: 4px;
    transform: rotate(-8deg);
    color: var(--card-white);
    font-size: 31px;
    font-weight: 400;
    line-height: 66px;
    text-align: center;
  }

  .brand-name {
    position: absolute;
    left: 0; right: 0;
    text-align: center;
    color: var(--brand-blue);
    font-weight: 500;
    letter-spacing: -0.5px;
  }
  .postcard--front .brand-name { top: 388px; font-size: 46px; }

  .forest-backdrop {
    position: absolute;
    inset: 0;
    background: linear-gradient(90deg, var(--forest-light) 0%, var(--forest-mid) 20%, var(--forest-light) 40%, var(--forest-mid) 60%, var(--forest-light) 80%, var(--forest-mid) 100%);
    opacity: 0.7;
  }
  .postcard--back .brand-name { top: 70px; font-size: 48px; }
  .back-headline {
    position: absolute;
    left: 0; right: 0;
    top: 215px;
    text-align: center;
    color: var(--brand-blue);
    font-size: 50px;
    font-weight: 400;
  }
  .contact {
    position: absolute;
    left: 0; right: 0;
    top: 345px;
    text-align: center;
    color: var(--ink-soft-blue);
    font-family: "Josefin Sans", "Century Gothic", sans-serif;
    font-weight: 300;
    font-size: 28px;
    line-height: 38px;
  }
</style>
</head>
<body>

  <section class="postcard postcard--front">
    <svg class="front-art" width="625" height="500" viewBox="0 0 625 500">
      <defs>
        <linearGradient id="ballPitTones" x1="0" y1="0" x2="1" y2="1">
          <stop offset="0" stop-color="var(--photo-red)"/>
          <stop offset="0.3" stop-color="var(--photo-purple)"/>
          <stop offset="0.5" stop-color="var(--photo-red)"/>
          <stop offset="0.7" stop-color="var(--photo-blue)"/>
          <stop offset="1" stop-color="var(--photo-green)"/>
        </linearGradient>
      </defs>
      <path class="photo-area-fill" role="img" aria-label="Photo of colourful play-pit balls in red, green, blue, purple and orange"
            d="M0 0 H625 V330 Q400 280 0 310 Z" fill="url(#ballPitTones)"/>
      <path class="band-blue" d="M0 305 Q400 275 625 325 V345 Q400 300 0 330 Z" fill="var(--brand-blue)"/>
      <path class="band-orange" d="M0 330 Q400 300 625 345 V358 Q400 316 0 342 Z" fill="var(--brand-orange)"/>
      <path class="card-base" d="M0 342 Q400 316 625 358 V500 H0 Z" fill="var(--card-white)"/>
    </svg>
    <div class="opening-tab">opening soon</div>
    <h1 class="brand-name">Brightleap Kids Gym</h1>
  </section>

  <section class="postcard postcard--back">
    <div class="forest-backdrop" role="img" aria-label="Soft faded wallpaper of a misty forest with tall tree trunks"></div>
    <h2 class="brand-name">Brightleap Kids Gym</h2>
    <p class="back-headline">opening soon</p>
    <address class="contact" style="font-style: normal;">
      www.brightleapgym.example<br>
      482 Maple Grove Lane<br>
      Fairview, CA 90000
    </address>
  </section>

</body>
</html>
```